E-Book/ Buch-Cover spannenden Liebesroman gesucht.
Zielgruppe
Ich bin Autorin und suche ein ansprechendes Cover für mein E-Book mit dem Titel:
' Schattenhafte Reue'. Es handelt sich um einen spannenden Liebesroman. Die emotionalen Ängste des Protagonisten, stehen neben den offensichtlichen Bedrohungen der Hauptfigur. Beide müssen ihren Weg zu einem Happyend finden. Da der Titel schon etwas „schreit“, sollte das Cover diesen Eindruck eventuell etwas abfedern.
Aufgabenstellung
Kein Kitsch, kein Schnulzencover, es handelt sich bei aller Dramatik trotzdem um einen Liebesroman. Keinen Thriller.

```html
<!DOCTYPE html>
<html lang="de">
<head>
<meta charset="utf-8">
<title>Schattenhafte Reue – c.m. sternfeld</title>
<link rel="stylesheet" href="https://fonts.googleapis.com/css2?family=Playfair+Display:wght@400;500;700&display=swap">
<style>
  :root {
    --sky-night: #0f1d24;
    --sky-deep: #1f3c45;
    --sky-teal: #3f6b74;
    --sky-haze: #8ea6aa;
    --sky-rose: #b79088;
    --sky-ember: #c8593a;
    --ground: #050505;
    --type: #ffffff;
  }
  * { margin: 0; padding: 0; box-sizing: border-box; }
  html, body {
    width: 750px;
    height: 1200px;
    overflow: hidden;
    background: var(--ground);
  }
  .cover {
    position: relative;
    width: 750px;
    height: 1200px;
    overflow: hidden;
    font-family: "Playfair Display", "Bodoni 72", Georgia, serif;
    color: var(--type);
  }
  .cover-scene {
    position: absolute;
    inset: 0;
    background: linear-gradient(
      to bottom,
      var(--sky-night) 0%,
      var(--sky-deep) 20%,
      var(--sky-teal) 38%,
      var(--sky-haze) 55%,
      var(--sky-rose) 66%,
      var(--sky-ember) 73%,
      #4a2a22 77%,
      var(--ground) 80%,
      var(--ground) 100%
    );
  }
  .title {
    position: absolute;
    left: 0;
    top: 0;
    width: 100%;
    font-weight: 400;
    line-height: 1;
  }
  .title-small {
    position: absolute;
    left: 139px;
    top: 120px;
    font-size: 78px;
    letter-spacing: -1px;
    white-space: nowrap;
  }
  .title-large {
    position: absolute;
    left: 30px;
    top: 118px;
    font-size: 320px;
    letter-spacing: -10px;
    line-height: 1;
    white-space: nowrap;
  }
  .genre {
    position: absolute;
    left: 498px;
    top: 540px;
    font-size: 44px;
    font-weight: 500;
    letter-spacing: 0.5px;
  }
  .author {
    position: absolute;
    left: 0;
    width: 100%;
    top: 1018px;
    text-align: center;
    font-size: 74px;
    font-weight: 400;
    letter-spacing: -0.5px;
  }
</style>
</head>
<body>
  <main class="cover">
    <div class="cover-scene" role="img" aria-label="Dämmerungshimmel über dunkler Landschaft mit Silhouette einer Frau mit wehendem Haar und einer Spur warmer Lichtpunkte"></div>
    <h1 class="title">
      <span class="title-large">Reue</span>
      <span class="title-small">Schattenhafte</span>
    </h1>
    <p class="genre">roman</p>
    <p class="author">c.m. sternfeld</p>
  </main>
</body>
</html>
```